Use Existing Logo to Design Letterhead, Envelope and Presentation Folder

We are a storm shelter company based out of Oklahoma City. We have an existing logo and brand image. We are looking for professionally designed letterhead, mailing envelopes and folders using our brand guidelines (attached). The font to be used is Futura.

The image represents simple professionalism.
We compete on quality, not price.
We value attention to detail and craftsmanship in our work.
The colors and layout are bold and clean.

Again, this is for:
1) Letterhead - contains name, address, phone, fax, and website address
2) Envelopes - logo, tagline and return address
3) Presentation Folders - logo and tag line

Our tag line is:
"Heartland's Finest Tornado Safe Rooms and Home Protection Products"

Please submit your designs and once we have the initial layouts, we will provide the top designers with our contact information.

Good luck!

```html
<!DOCTYPE html>
<html lang="en">
<head>
<meta charset="utf-8">
<title>Keystone Shelters Stationery</title>
<link rel="stylesheet" href="https://fonts.googleapis.com/css2?family=Jost:wght@400;500;600&display=swap">
<style>
  :root {
    --backdrop: #4a1520;
    --brand-blue: #2b3a97;
    --brand-grey: #959595;
    --rule-grey: #b9b9c4;
    --paper: #ffffff;
    --faint-grey: #e4e4e4;
    --faint-lavender: #d9d9ee;
    --text-dark: #3c3c3c;
  }
  * { box-sizing: border-box; margin: 0; padding: 0; }
  html, body { width: 1071px; height: 1200px; overflow: hidden; }
  body {
    position: relative;
    background: var(--backdrop);
    font-family: "Jost", "Futura", sans-serif;
    color: var(--text-dark);
  }
  .piece { position: absolute; background: var(--paper); overflow: hidden; }
  .band { position: absolute; left: 0; right: 0; background: var(--brand-blue); }
  .band-rule { position: absolute; left: 0; right: 0; height: 1px; background: var(--rule-grey); }
  .brand-name {
    position: absolute;
    font-weight: 500;
    letter-spacing: 0.06em;
    text-transform: uppercase;
    line-height: 1.1;
    white-space: nowrap;
  }
  .brand-name.on-paper { color: var(--brand-blue); }
  .brand-name.on-colour { color: var(--paper); }
  .brand-name.faint { color: var(--faint-lavender); }
  .centred { left: 0; right: 0; text-align: center; }
  .tagline { position: absolute; color: var(--brand-blue); font-weight: 500; white-space: nowrap; }
  .small-text { position: absolute; white-space: nowrap; color: var(--text-dark); }
  .contact-line { display: flex; align-items: center; gap: 4px; }
  .contact-icon { width: 8px; height: 8px; border-radius: 50%; background: currentColor; display: inline-block; }

  /* Letterhead */
  .letterhead { left: 35px; top: 29px; width: 427px; height: 553px; }
  .letterhead .band { top: 0; height: 35px; }
  .letterhead .band-rule { top: 38px; }
  .letterhead .brand-name.masthead { left: 13px; top: 56px; font-size: 13px; }
  .letterhead .contacts { position: absolute; left: 317px; top: 7px; border-left: 1px solid var(--paper);
    padding-left: 6px; color: var(--paper); font-size: 7px; line-height: 11px; }
  .letterhead .tagline { right: 11px; top: 42px; font-size: 7.5px; }
  .letterhead .watermark { top: 292px; font-size: 26px; }
  .letterhead .footer-address { left: 0; right: 0; bottom: 8px; text-align: center; font-size: 8px; }

  /* Envelopes */
  .envelope { border: 1px solid #cfcfcf; }
  .envelope svg { position: absolute; left: 0; top: 0; }
  .envelope-back { left: 567px; top: 122px; width: 477px; height: 213px; }
  .envelope-back .brand-name { top: 38px; font-size: 12px; }
  .envelope-middle { left: 543px; top: 231px; width: 478px; height: 212px; }
  .envelope-middle .brand-name { top: 32px; font-size: 12px; }
  .envelope-front { left: 516px; top: 327px; width: 478px; height: 214px; }
  .envelope-front .band { top: 0; height: 36px; }
  .envelope-front .band-rule { top: 40px; }
  .envelope-front .brand-name.masthead { left: 14px; top: 58px; font-size: 11px; }
  .envelope-front .return-address { left: 14px; top: 86px; font-size: 7px; line-height: 9px; }
  .envelope-front .web { left: 8px; bottom: 9px; font-size: 8px; font-weight: 500; letter-spacing: 0.03em; }
  .envelope-front .watermark { right: 18px; top: 160px; font-size: 13px; }

  /* Folder */
  .folder-panel { top: 600px; height: 576px; }
  .folder-left { left: 227px; width: 363px; }
  .folder-right { left: 590px; width: 361px; border-left: 1px solid #d6d6d6; }
  .folder-left .watermark { top: 130px; font-size: 26px; color: var(--faint-grey); }
  .folder-left .brand-name.primary { top: 333px; font-size: 33px; }
  .folder-left .divider { position: absolute; left: 46px; right: 46px; top: 414px; height: 1px; background: #c6c6c6; }
  .folder-left .folder-contacts { left: 0; right: 0; top: 424px; text-align: center; font-size: 10px; line-height: 17px; }
  .folder-left .folder-contacts .contact-line { justify-content: center; gap: 12px; }
  .folder-pocket { position: absolute; top: 468px; height: 108px; }
  .folder-left .folder-pocket { left: 0; width: 363px; background: var(--brand-blue); border-bottom-right-radius: 104px 104px; }
  .folder-right .folder-pocket { left: 0; width: 361px; background: var(--brand-grey); border-bottom-left-radius: 104px 104px; }
  .folder-pocket .brand-name { top: 44px; font-size: 15px; }
  .folder-right .band { top: 0; height: 62px; }
  .folder-right .band-rule { top: 66px; }
  .folder-right .brand-name.primary { top: 120px; font-size: 30px; }
  .folder-right .tagline { left: 0; right: 0; top: 449px; text-align: center; font-size: 8px; }
</style>
</head>
<body>

<section class="piece letterhead">
  <div class="band"></div>
  <div class="band-rule"></div>
  <div class="contacts">
    <div class="contact-line"><span class="contact-icon"></span>012-555-0147</div>
    <div class="contact-line"><span class="contact-icon"></span>www.keystoneshelters.com</div>
  </div>
  <p class="brand-name on-paper masthead">Keystone<br>Shelters</p>
  <p class="tagline">Heartland's Finest Tornado Safe Rooms and Home Protection Products</p>
  <p class="brand-name faint watermark centred">Keystone Shelters</p>
  <p class="small-text footer-address">Street Name, City Name, Zip Code - 12345</p>
</section>

<section class="piece envelope envelope-back">
  <svg width="477" height="213" viewBox="0 0 477 213">
    <path d="M0 0 L200 78 Q243 90 286 78 L477 0" fill="none" stroke="#555" stroke-width="0.8"/>
  </svg>
  <p class="brand-name on-paper centred">Keystone Shelters</p>
</section>

<section class="piece envelope envelope-middle">
  <svg width="478" height="212" viewBox="0 0 478 212">
    <path d="M0 0 H478 L474 28 Q468 42 440 48 L275 80 Q247 86 219 80 L40 46 Q8 40 2 22 Z" fill="var(--brand-grey)"/>
  </svg>
  <p class="brand-name on-colour centred">Keystone Shelters</p>
</section>

<section class="piece envelope envelope-front">
  <div class="band"></div>
  <div class="band-rule"></div>
  <p class="brand-name on-paper masthead">Keystone<br>Shelters</p>
  <p class="small-text return-address">Street Name, City Name<br>Zip Code - 12345</p>
  <p class="small-text web">www.keystoneshelters.com</p>
  <p class="brand-name faint watermark">Keystone</p>
</section>

<section class="piece folder-panel folder-left">
  <p class="brand-name watermark centred">Keystone Shelters</p>
  <p class="brand-name on-paper primary centred">Keystone<br>Shelters</p>
  <div class="divider"></div>
  <div class="small-text folder-contacts">
    <div>Street Name, City Name, Zip Code - 12345</div>
    <div class="contact-line"><span>012-555-0147</span><span>www.keystoneshelters.com</span></div>
  </div>
  <div class="folder-pocket"><p class="brand-name on-colour centred">Keystone Shelters</p></div>
</section>

<section class="piece folder-panel folder-right">
  <div class="band"></div>
  <div class="band-rule"></div>
  <p class="brand-name on-paper primary centred">Keystone<br>Shelters</p>
  <p class="tagline">Heartland's Finest Tornado Safe Rooms and Home Protection Products</p>
  <div class="folder-pocket"><p class="brand-name on-colour centred">Keystone Shelters</p></div>
</section>

</body>
</html>
```